Investment Company Business Card Design

We need a Business Card design for a new company based in Boston called "Velm Investment". We are cooperating with local real estate and construction companies. Our company is very actively and aggressively acquiring primarily residential investment properties either to buy and hold long term or for purposes or renovating and repositioning for re-sale in the market. In addition, we undertake some development projects and acquisitions as opportunities present themselves. the final design should contains information about “Velm" the river boat. we are tenacious, indomitable, and the business have a favorable wind throughout the voyage for all our investment.
sample Info. on Design:
Tusa Merrick
CEO
555-xxx-xxxx
418 Harlow St. Suite 507, Boston, MA 02111
Please provide a template also, that we can edit the info later.
Reason: i just got new LOGO Design attached will be use in Business Card Design.
Construction

```html
<!DOCTYPE html>
<html lang="en">
<head>
<meta charset="utf-8">
<title>Velm Investment – Business Card</title>
<link href="https://fonts.googleapis.com/css2?family=Exo+2:wght@400;500;600&display=swap" rel="stylesheet">
<style>
  :root {
    --page: #ecebe8;
    --card: #ffffff;
    --gold-light: #e6c77f;
    --gold: #d2a95a;
    --gold-deep: #b98f3e;
    --ink: #2b2b2b;
    --ink-soft: #555555;
  }
  * { box-sizing: border-box; margin: 0; padding: 0; }
  html, body { width: 1200px; height: 900px; overflow: hidden; }
  body {
    background: var(--page);
    font-family: "Exo 2", sans-serif;
    color: var(--ink);
    position: relative;
  }
  .card {
    position: absolute;
    left: 250px;
    width: 700px;
    height: 400px;
    background: var(--card);
    box-shadow: 0 6px 18px rgba(0,0,0,.18);
    overflow: hidden;
  }
  .card--front { top: 35px; }
  .card--back  { top: 465px; }

  .card__panel {
    position: absolute;
    left: 0; top: 0;
    width: 700px;
    height: 180px;
    background: linear-gradient(160deg, var(--gold-deep) 0%, var(--gold-light) 60%, var(--gold) 100%);
  }

  .contact {
    position: absolute;
    left: 40px;
    top: 26px;
    list-style: none;
    font-size: 15px;
    letter-spacing: .5px;
    color: var(--ink);
  }
  .contact__item {
    display: flex;
    align-items: center;
    gap: 12px;
    height: 25px;
  }
  .contact__icon { width: 15px; height: 15px; fill: var(--ink); flex: none; }

  .address {
    position: absolute;
    right: 34px;
    top: 102px;
    font-size: 14px;
    letter-spacing: .4px;
    color: var(--ink);
  }

  .holder {
    position: absolute;
    left: 40px;
    top: 238px;
  }
  .holder__name {
    font-size: 26px;
    font-weight: 500;
    letter-spacing: 2px;
    text-transform: uppercase;
  }
  .holder__title {
    font-size: 17px;
    margin-top: 6px;
    color: var(--ink-soft);
  }

  .brand {
    position: absolute;
    display: flex;
    align-items: center;
    gap: 12px;
    white-space: nowrap;
    font-weight: 600;
    letter-spacing: 1.5px;
    color: var(--gold-deep);
  }
  .brand__mark {
    width: 16px; height: 16px;
    border-radius: 50%;
    background: var(--gold-deep);
    flex: none;
  }
  .card--front .brand { right: 40px; bottom: 40px; font-size: 26px; }
  .card--back .brand  { left: 50%; top: 50%; transform: translate(-50%, -50%); font-size: 40px; }
</style>
</head>
<body>

<section class="card card--front">
  <div class="card__panel" role="img" aria-label="Gold decorative band across the top of the card"></div>

  <ul class="contact">
    <li class="contact__item">
      <svg class="contact__icon" viewBox="0 0 16 16"><path d="M3 1l3 3-1.5 2a9 9 0 0 0 5.5 5.5L12 10l3 3-2 2C6 14 2 10 1 3z"/></svg>
      555-xxx-xxxx
    </li>
    <li class="contact__item">
      <svg class="contact__icon" viewBox="0 0 16 16"><path d="M4 0h8v16H4zM5.5 2v10h5V2zM7 13.5h2v1H7z" fill-rule="evenodd"/></svg>
      555-xxx-xxxx
    </li>
    <li class="contact__item">
      <svg class="contact__icon" viewBox="0 0 16 16"><path d="M1 5h14v9H1zM4 1h8v4H4zM3 8h3v1H3zM3 10h3v1H3z"/></svg>
      555-xxx-xxxx
    </li>
    <li class="contact__item">
      <svg class="contact__icon" viewBox="0 0 16 16"><path d="M1 3h14v10H1zM2.5 4.5L8 9l5.5-4.5v7h-11z" fill-rule="evenodd"/></svg>
      tusa@velminvest.com
    </li>
    <li class="contact__item">
      <svg class="contact__icon" viewBox="0 0 16 16"><path d="M8 1a7 7 0 1 0 0 14A7 7 0 0 0 8 1zm0 1.5c1 0 2 2 2.3 4.7H5.7C6 4.5 7 2.5 8 2.5zM5.7 8.8h4.6C10 11.5 9 13.5 8 13.5S6 11.5 5.7 8.8zM2.6 7.2a5.5 5.5 0 0 1 2.3-3.8 9 9 0 0 0-.8 3.8zm0 1.6h1.5a9 9 0 0 0 .8 3.8 5.5 5.5 0 0 1-2.3-3.8zm10.8-1.6h-1.5a9 9 0 0 0-.8-3.8 5.5 5.5 0 0 1 2.3 3.8zm0 1.6a5.5 5.5 0 0 1-2.3 3.8 9 9 0 0 0 .8-3.8z" fill-rule="evenodd"/></svg>
      www.velminvest.com
    </li>
  </ul>

  <p class="address">418 Harlow St. Suite 507, Boston, MA 02111</p>

  <div class="holder">
    <h1 class="holder__name">Tusa Merrick</h1>
    <p class="holder__title">CEO</p>
  </div>

  <div class="brand"><span class="brand__mark"></span>Velm Investment</div>
</section>

<section class="card card--back">
  <div class="brand"><span class="brand__mark"></span>Velm Investment</div>
</section>

</body>
</html>
```